Tamarack Hearth Partners Business Card

Looking for a new business card layout. We are a real estate firm w/ a logo, old design attached. Must keep the same elements on there, just need a fresh look and possible some foil accents. Looking for a simpler design w/ more modern style.

Target Market(s)

Real Estate clients

Industry/Entity Type

Real Estate Agent

Contact Information for Business Card

see attached

Font styles to use
Sans Serif

Requirements
Must have
• all elements on current biz card
Nice to have
• modern look, simpler than we have!
Should not have
• no serif fonts

```html
<!DOCTYPE html>
<html lang="en">
<head>
<meta charset="utf-8">
<title>Tamarack Hearth Partners – Business Card</title>
<link href="https://fonts.googleapis.com/css2?family=Ubuntu:wght@400;500&family=Josefin+Sans:wght@300&display=swap" rel="stylesheet">
<style>
  :root {
    --frame: #2a2928;
    --card-dark: #2a2928;
    --paper: #ffffff;
    --band: #b2b4b3;
    --ink-light: #ffffff;
    --silver: #a3a5a5;
    --rule: #2a2928;
  }
  html, body { margin: 0; padding: 0; overflow: hidden; }
  body { width: 1200px; height: 1200px; background: var(--frame); font-family: "Ubuntu", sans-serif; }
  .board { position: relative; width: 1200px; height: 1200px; }
  .sheet { position: absolute; left: 27px; top: 27px; width: 1146px; height: 1146px; background: var(--paper); }
  .band { position: absolute; left: 27px; top: 547px; width: 1146px; height: 520px; background: var(--band); }

  .card { position: absolute; box-sizing: border-box; }
  .card--dark { background: var(--card-dark); color: var(--ink-light); }
  .card--light { background: var(--paper); }

  .portrait {
    left: 383px; top: 161px; width: 144px; height: 252px;
    background: linear-gradient(180deg, #ece6dc 0%, #e3cfa8 35%, #e0b9a2 60%, #3fbcc3 85%, #2cc3c9 100%);
  }

  .name { position: absolute; font-weight: 500; font-size: 12.5px; line-height: 1; white-space: nowrap; }
  .role { position: absolute; font-size: 6.5px; letter-spacing: 0.2px; white-space: nowrap; }
  .contact { position: absolute; font-size: 8.6px; line-height: 10.5px; white-space: nowrap; }
  .contact .label { display: inline-block; width: 28px; font-size: 6.5px; }
  .contact .row { display: block; }
  .line { position: absolute; font-size: 8.6px; line-height: 10.5px; white-space: nowrap; }

  .wordmark { position: absolute; color: var(--silver); font-family: "Ubuntu", sans-serif; font-weight: 500; text-transform: uppercase; line-height: 1.05; white-space: nowrap; text-align: center; }

  /* vertical card */
  .card-tall { left: 673px; top: 161px; width: 144px; height: 252px; }
  .card-tall .name { left: 8px; top: 14px; }
  .card-tall .role { left: 8px; top: 28px; }
  .card-tall .contact { left: 8px; top: 53px; }
  .card-tall .web { left: 8px; top: 105px; }
  .card-tall .address { left: 8px; top: 137px; }
  .card-tall .wordmark { left: 0; width: 144px; top: 221px; font-size: 11px; letter-spacing: 0.6px; }

  /* horizontal front */
  .card-front { left: 329px; top: 735px; width: 252px; height: 144px; }
  .card-front .wordmark { left: 0; width: 252px; top: 48px; font-size: 16px; letter-spacing: 1px; }
  .card-front .url { position: absolute; left: 0; width: 252px; top: 102px; text-align: center; font-family: "Josefin Sans", sans-serif; font-weight: 300; font-size: 9.5px; letter-spacing: 1.6px; color: #2a2928; }

  /* horizontal back */
  .card-back { left: 619px; top: 735px; width: 252px; height: 144px; }
  .card-back .wordmark-rotated { position: absolute; left: 18px; top: 72px; width: 124px; transform: translate(-50%, -50%) rotate(-90deg); transform-origin: center; left: 28px; font-size: 10px; letter-spacing: 0.5px; }
  .card-back .name { left: 118px; top: 15px; }
  .card-back .role { left: 118px; top: 29px; }
  .card-back .contact { left: 118px; top: 44px; }
  .card-back .address { left: 118px; top: 108px; }

  /* foil legend */
  .legend-mark { position: absolute; left: 400px; top: 1090px; width: 400px; font-size: 27px; letter-spacing: 2px; line-height: 1.1; }
  .legend-rule { position: absolute; left: 830px; top: 1085px; width: 1.5px; height: 70px; background: var(--rule); }
  .legend-label { position: absolute; left: 874px; top: 1111px; font-size: 15px; letter-spacing: 2px; word-spacing: 8px; color: var(--rule); }
</style>
</head>
<body>
<main class="board">
  <div class="sheet"></div>
  <div class="band"></div>

  <div class="card portrait" role="img" aria-label="Portrait photo of the broker, smiling, in a teal top"></div>

  <section class="card card--dark card-tall">
    <div class="name">Dana Whitlow</div>
    <div class="role">Principal Broker</div>
    <div class="contact">
      <span class="row"><span class="label">cell</span>555.014.2290</span>
      <span class="row"><span class="label">office</span>555.014.7310</span>
      <span class="row">dana@hearthpartners.com</span>
    </div>
    <div class="line web">TamarackHearth-Homes.com</div>
    <div class="line address">240 Pine Ridge Ave.,<br>Larchmont, OR 97000</div>
    <div class="wordmark">Tamarack Hearth<br>Partners</div>
  </section>

  <section class="card card--light card-front">
    <div class="wordmark">Tamarack Hearth<br>Partners</div>
    <div class="url">TAMARACKHEARTH-HOMES.COM</div>
  </section>

  <section class="card card--dark card-back">
    <div class="wordmark wordmark-rotated">Tamarack Hearth<br>Partners</div>
    <div class="name">Dana Whitlow</div>
    <div class="role">Principal Broker</div>
    <div class="contact">
      <span class="row"><span class="label">cell</span>555.014.2290</span>
      <span class="row"><span class="label">office</span>555.014.7310</span>
      <span class="row"><span class="label"></span>dana@hearthpartners.com</span>
    </div>
    <div class="line address">240 Pine Ridge Ave.,<br>Larchmont, OR 97000</div>
  </section>

  <div class="wordmark legend-mark">Tamarack Hearth<br>Partners</div>
  <div class="legend-rule"></div>
  <div class="legend-label">SILVER FOIL</div>
</main>
</body>
</html>
```